Refer a friend or family in July 2014

We offer the following classrooms to suit ALL your needs.

Please put in table or in a clear format so parents can read this information

Before school care $35 or after rebates $17.50 per morning
Long day / vacation care $110 per day or after rebates $55.00 per day
Early morning Half day / vacation care (6.00am to 2.30pm) $80 per day or after rebates $40 per day
Half day / vacation care $60 per day (8.30am to 2.00pm) or after rebates $30 per day Vacation care half day 6am to 12pm or 12pm to 5.30pm $55 or $27.50 after rebates
After school care $45.00 or after rebate $22.50 per day

* Terms and Conditions – Family Referral Form
1. Offer valid till 31 August 2014
2. New Child must be enrolled for a minimum of 2 days per week and a 4 week period minimum before credit is applied
3. The $50 account credit will be added 5 weeks after referring family/families have started at Gathering Sprouts Velvet Otters Junior Education Centre.
4. The credit cannot be refunded as cash and is only a credit on their current account.
5. Discount offer applies only to all new referred children.
6. Existing children enrolled or siblings of current families at the centre are not eligible for this offer.

Target Market(s)

parents

Industry/Entity Type

School

Font styles to use
Sans Serif

Requirements
Must have
• refer a friend or family in July !

childcare local to you.

children learn, laugh and have fun!

be professional and corporate over "colourful and too childcare like " this is for parents

flexible times to suit you.

qualified teachers

get ready for school program - pre -kindergarten classroom

www.gatheringsprouts-example.com.au

0461735208
Should not have
• too much colour to messy - unclear..

```html
<!DOCTYPE html>
<html lang="en">
<head>
<meta charset="utf-8">
<title>Refer a friend or family in July</title>
<link href="https://fonts.googleapis.com/css2?family=Kalam:wght@300;400&family=PT+Sans:ital,wght@0,400;0,700;1,400;1,700&display=swap" rel="stylesheet">
<style>
  :root {
    --stage: #3b3b3b;
    --green: #8cb13f;
    --green-dark: #4f7e1e;
    --purple: #6d4f9c;
    --purple-dark: #51307f;
    --purple-text: #5b3e8c;
    --paper: #ffffff;
    --mist: #e9e9ec;
    --ink: #3a3a3a;
  }
  * { margin: 0; padding: 0; box-sizing: border-box; }
  html, body { width: 882px; height: 1200px; overflow: hidden; }
  body { background: var(--stage); position: relative; font-family: "PT Sans", sans-serif; }

  .flyer {
    position: absolute; left: 31px; top: 19px;
    width: 820px; height: 1162px;
    background: linear-gradient(180deg, var(--paper) 0%, var(--mist) 100%);
    overflow: hidden;
  }
  .flyer > * { position: absolute; }

  .header-band { left: 0; top: 0; width: 820px; height: 265px; background: var(--green); }
  .headline {
    left: 0; top: 18px; width: 820px; text-align: center;
    font-family: "Kalam", cursive; font-weight: 400; font-size: 50px;
    color: var(--paper); font-style: italic; letter-spacing: 0.5px;
  }
  .hero-photo {
    left: 51px; top: 99px; width: 732px; height: 290px;
    border: 4px solid var(--paper);
    background: linear-gradient(90deg, #c7b7d9 0%, #d9cbe6 45%, #b98f7a 75%, #c99a8d 100%);
    box-shadow: 0 6px 8px rgba(0,0,0,0.25);
  }
  .subheading-band { left: 0; top: 397px; width: 820px; height: 51px; background: #e4e4e4; }
  .subheading {
    left: 0; top: 405px; width: 820px; text-align: center;
    font-family: "Kalam", cursive; font-weight: 300; font-size: 24px;
    color: var(--ink); font-style: italic;
  }

  .shapes { left: 0; top: 0; width: 820px; height: 1162px; }

  .fees-title {
    left: 72px; top: 456px; font-weight: 700; font-size: 25px; line-height: 34px; color: var(--paper);
  }
  .fees-list { left: 66px; top: 495px; list-style: none; }
  .fees-list li {
    font-size: 14.8px; line-height: 21.8px; font-style: italic; font-weight: 700; color: var(--paper);
    white-space: nowrap;
  }
  .fees-list .rule { display: inline-block; width: 150px; height: 2px; background: var(--purple); vertical-align: middle; margin-left: 8px; position: relative; }
  .fees-list .rule::after { content: ""; position: absolute; right: -3px; top: -2px; width: 6px; height: 6px; border-radius: 50%; background: var(--purple); }

  .terms-title {
    left: 20px; top: 704px; font-size: 19.5px; line-height: 26px; font-style: italic; font-weight: 700; color: var(--paper);
  }
  .terms-list { left: 32px; top: 731px; list-style: none; }
  .terms-list li {
    font-size: 16px; line-height: 22.8px; font-weight: 700; color: var(--paper); white-space: nowrap;
  }

  .circle-photo {
    left: 544px; top: 638px; width: 238px; height: 238px; border-radius: 50%;
    border: 8px solid #8e74b4;
    background: linear-gradient(135deg, #3f4f8e 0%, #7d8cc2 45%, #e9dcc9 75%, #c9a98c 100%);
    box-shadow: 0 0 0 3px var(--paper);
  }

  .tagline {
    right: 19px; height: 28px; text-align: right;
    font-family: "Kalam", cursive; font-weight: 300; font-style: italic;
    font-size: 18px; line-height: 28px; color: var(--purple-text);
    padding-right: 12px; border-bottom: 2px solid var(--purple);
  }
  .tagline::after {
    content: ""; position: absolute; right: -4px; bottom: -5px;
    width: 8px; height: 8px; border-radius: 50%; background: var(--purple);
  }
  .tagline-teachers { top: 881px; width: 167px; }
  .tagline-local { top: 910px; width: 183px; }
  .tagline-flexible { top: 938px; width: 211px; }
  .tagline-fun { top: 969px; width: 319px; }
  .tagline-school { top: 1003px; width: 485px; }

  .play-photo {
    left: 0; top: 990px; width: 820px; height: 141px;
    background: linear-gradient(90deg, #d7dde6 0%, #e8e1da 40%, #dcdfe8 70%, #e5e5ea 100%);
    opacity: 0.9;
  }
  .centre-name {
    left: 21px; top: 1004px; width: 151px; height: 121px;
    background: var(--purple); display: flex; align-items: center; justify-content: center;
    text-align: center; padding: 10px;
    font-size: 13px; line-height: 16px; font-weight: 700; color: var(--paper);
    box-shadow: 0 2px 5px rgba(0,0,0,0.3);
  }
  .phone-bar {
    left: 427px; top: 1057px; width: 393px; height: 61px;
    background: rgba(255,255,255,0.85);
    display: flex; align-items: center; gap: 10px; padding-left: 6px;
  }
  .phone-bar svg { flex: none; }
  .phone-number { font-size: 52px; color: var(--purple-text); letter-spacing: 0.5px; line-height: 1; }

  .footer-band {
    left: 0; top: 1131px; width: 820px; height: 31px; background: var(--green);
    text-align: center; color: var(--paper); font-size: 20px; line-height: 31px; letter-spacing: 4px;
  }
</style>
</head>
<body>
<main class="flyer">
  <div class="header-band"></div>
  <h1 class="headline">Refer a friend or family in July !</h1>
  <div class="hero-photo" role="img" aria-label="Photo of a teacher doing a craft activity at a table with toddlers in sun hats"></div>
  <div class="subheading-band"></div>
  <p class="subheading">We offer the following classrooms to suit ALL your needs.</p>

  <div class="play-photo" role="img" aria-label="Faded photo of children on a climbing frame in the playground"></div>

  <svg class="shapes" viewBox="0 0 820 1162" aria-hidden="true">
    <polygon points="0,465 22,465 40,448 58,465 615,465 640,695 0,695" fill="var(--green)"/>
    <polygon points="55,454 608,454 614,491 55,491" fill="var(--green-dark)"/>
    <polygon points="0,695 640,695 470,990 0,990" fill="var(--purple)"/>
    <polygon points="8,705 560,705 550,730 8,730" fill="var(--purple-dark)"/>
  </svg>

  <h2 class="fees-title">Session full fees after rebates</h2>
  <ul class="fees-list">
    <li>Before school care $35 or after rebates $17.50 per morning</li>
    <li>Long day / vacation care $110 per day or after rebates $55.00 per day</li>
    <li>Early morning Half day / vacation care (6.00am to 2.30pm) $80 per day or</li>
    <li>after rebates $40 per day</li>
    <li>Half day / vacation care $60 per day (8.30am to 2.00pm) or after rebates $30 per day</li>
    <li>After school care $45.00 or after rebate $22.50 per day</li>
    <li>Vacation care two sessions<span class="rule"></span></li>
    <li>Morning 6am to 12pm $55 per morning after rebates $27.50</li>
    <li>Afternoon 12pm to 5.30pm $55 per afternoon after rebates</li>
  </ul>

  <h2 class="terms-title">* Terms and Conditions – Family Referral Form</h2>
  <ol class="terms-list">
    <li>1. Offer valid till 31 July 2014</li>
    <li>2. New Child must be enrolled for a minimum of 2 days per week and a 4<br>week period minimum before credit is applied</li>
    <li>3. The $50 account credit will be added 5 weeks after referring<br>family/families have started at Gathering Sprouts Velvet Otters Junior<br>Education Centre.</li>
    <li>4. The credit cannot be refunded as cash and is only a credit on their<br>current account.</li>
    <li>5. Discount offer applies only to all new referred children.</li>
    <li>6. Existing children enrolled or siblings of current families at<br>the centre are not eligible for this offer.</li>
  </ol>

  <div class="circle-photo" role="img" aria-label="Round photo of a teacher helping children with a science activity"></div>

  <p class="tagline tagline-teachers">qualified teachers</p>
  <p class="tagline tagline-local">childcare local to you</p>
  <p class="tagline tagline-flexible">flexible times to suit you</p>
  <p class="tagline tagline-fun">children learn, laugh and have fun!</p>
  <p class="tagline tagline-school">get ready for school program - pre -kindergarten classroom</p>

  <div class="centre-name">Gathering Sprouts Velvet Otters Junior Education Centre</div>

  <div class="phone-bar">
    <svg width="50" height="50" viewBox="0 0 54 54" aria-hidden="true">
      <circle cx="27" cy="27" r="26" fill="#555"/>
      <path d="M19 14c2-1 3 0 4 2l2 5c1 2 0 3-1 4l-2 2c2 4 5 7 9 9l2-2c1-1 2-2 4-1l5 2c2 1 3 2 2 4l-1 3c-1 2-3 3-6 2-10-3-17-10-20-20-1-3 0-5 2-6z" fill="#fff"/>
    </svg>
    <span class="phone-number">0461735208</span>
  </div>

  <footer class="footer-band">www.gatheringsprouts-example.com.au</footer>
</main>
</body>
</html>
```